Create a flyer for our party getaway to Ibiza.

'The Crimson Ibiza Escape'

Friday 14th July - Monday 17th July

DJ Morvek & DJ Tundral brings together a jam-packed weekend schedule full of the best urban parties in Ibiza.

What's included?

4 Nights Of Entertainment
6 Parties In Total
1 Boat Party
1 Pool Party
2 Superclub Parties
1 Indoor Water Party
Bottomless Drinks (Boat Party Only)
An unbelievable experience
1 unbeatable price.

All this for 140€ (you save 50€ when you book with us)

Tickets avaialble from Ticketlane & Gribolo

Target Market(s)

holiday goers

Industry/Entity Type

party, events, club, hip hop

Requirements
Must have
• good vibes
Nice to have
• nice catchy looking title

```html
<!DOCTYPE html>
<html lang="en">
<head>
<meta charset="utf-8">
<title>The Crimson Ibiza Escape – Flyer</title>
<link rel="stylesheet" href="https://fonts.googleapis.com/css2?family=Russo+One&family=Comfortaa:wght@500;700&display=swap">
<style>
  :root {
    --night: #2a0b4a;
    --violet: #5a1a86;
    --magenta: #c21fb8;
    --hot-pink: #e52fd6;
    --amber: #b5552e;
    --cyan: #16f4f4;
    --mint: #2de6a9;
    --ring-blue: #3b4cff;
    --ring-purple: #8b2cf0;
    --title-white: #eef0fb;
    --title-shade: #b8bcd8;
    --yellow: #f4f423;
    --panel: rgba(236, 140, 236, 0.42);
    --text-white: #ffffff;
  }
  * { margin: 0; padding: 0; box-sizing: border-box; }
  html, body { width: 871px; height: 1200px; overflow: hidden; background: #e9e9eb; }
  .flyer {
    position: relative;
    width: 871px;
    height: 1200px;
    overflow: hidden;
    background:
      radial-gradient(ellipse at 100% 100%, var(--amber) 0%, rgba(181,85,46,0) 45%),
      radial-gradient(ellipse at 0% 100%, var(--hot-pink) 0%, rgba(229,47,214,0) 50%),
      linear-gradient(170deg, var(--night) 0%, var(--violet) 30%, #7b1a8e 60%, #8e1c86 100%);
    font-family: "Comfortaa", sans-serif;
    color: var(--text-white);
  }
  .brush-band {
    position: absolute;
    left: -40px;
    width: 960px;
    height: 60px;
    background: linear-gradient(90deg, rgba(214,80,200,0.35), rgba(140,60,220,0.1));
    transform: rotate(-12deg);
  }
  .headliners {
    position: absolute;
    top: 44px;
    left: 0;
    width: 871px;
    text-align: center;
    font-family: "Russo One", sans-serif;
    font-size: 50px;
    font-weight: 400;
    letter-spacing: 1px;
    color: var(--text-white);
    text-shadow: 0 0 10px rgba(255,255,255,0.5);
  }
  .headliners-tagline {
    position: absolute;
    top: 114px;
    left: 0;
    width: 871px;
    text-align: center;
    font-family: "Russo One", sans-serif;
    font-size: 12.5px;
    letter-spacing: 0.2px;
    color: var(--text-white);
  }
  .decor { position: absolute; inset: 0; }
  .event-title {
    position: absolute;
    font-family: "Russo One", sans-serif;
    font-weight: 400;
    color: var(--title-white);
    background: linear-gradient(180deg, var(--text-white) 20%, var(--title-shade) 100%);
    -webkit-background-clip: text;
    background-clip: text;
    -webkit-text-fill-color: transparent;
    filter: drop-shadow(4px 6px 4px rgba(40,0,60,0.55));
    transform-origin: left bottom;
    white-space: nowrap;
    line-height: 1;
  }
  .event-title--top { left: 160px; top: 598px; font-size: 92px; transform: rotate(-11deg) scaleX(0.8); }
  .event-title--bottom { left: 80px; top: 738px; font-size: 112px; transform: rotate(-11deg) scaleX(0.8); }
  .included {
    position: absolute;
    left: 23px;
    top: 865px;
    width: 348px;
    height: 340px;
    background: var(--panel);
    border-radius: 30px 30px 0 0;
    padding: 30px 0 0 24px;
  }
  .included-heading { font-size: 26px; font-weight: 700; margin-bottom: 10px; }
  .included-list { list-style: none; font-size: 14.5px; font-weight: 500; line-height: 26.5px; }
  .dates {
    position: absolute;
    font-family: "Russo One", sans-serif;
    font-size: 43px;
    line-height: 1;
    text-align: right;
    white-space: nowrap;
    background: linear-gradient(90deg, var(--cyan), var(--mint));
    -webkit-background-clip: text;
    background-clip: text;
    -webkit-text-fill-color: transparent;
    filter: drop-shadow(2px 3px 2px rgba(30,0,50,0.6));
  }
  .dates--start { top: 866px; right: 36px; }
  .dates--end { top: 929px; right: 26px; }
  .offer {
    position: absolute;
    right: 27px;
    text-align: right;
    white-space: nowrap;
    font-family: "Comfortaa", sans-serif;
    font-weight: 700;
  }
  .offer-price { top: 992px; font-size: 50px; color: var(--yellow); }
  .offer-saving { top: 1065px; font-size: 18px; font-weight: 500; color: var(--text-white); }
  .offer-tickets { top: 1094px; font-size: 30px; color: var(--yellow); }
  .offer-sellers { top: 1134px; font-size: 29px; color: var(--text-white); }
  .offer-sellers .arrows { font-size: 14px; vertical-align: middle; margin-right: 4px; }
</style>
</head>
<body>
<main class="flyer">
  <div class="brush-band" style="top:150px;"></div>
  <div class="brush-band" style="top:230px; opacity:.6;"></div>
  <div class="brush-band" style="top:470px; opacity:.5;"></div>

  <h2 class="headliners">DJ MORVEK &amp; DJ TUNDRAL</h2>
  <p class="headliners-tagline">BRINGS TOGETHER A JAM-PACKED WEEKEND SCHEDULE FULL OF THE BEST URBAN PARTIES IN IBIZA</p>

  <svg class="decor" width="871" height="1200" viewBox="0 0 871 1200">
    <defs>
      <linearGradient id="ring" x1="0" y1="0" x2="1" y2="1">
        <stop offset="0" stop-color="var(--cyan)"/>
        <stop offset="0.5" stop-color="var(--ring-blue)"/>
        <stop offset="1" stop-color="var(--ring-purple)"/>
      </linearGradient>
      <linearGradient id="photo-tone" x1="0" y1="0" x2="1" y2="1">
        <stop offset="0" stop-color="#c23a4a"/>
        <stop offset="0.45" stop-color="#d7d3ee"/>
        <stop offset="1" stop-color="#2b2f6e"/>
      </linearGradient>
      <linearGradient id="tri-top" x1="0" y1="0" x2="1" y2="1">
        <stop offset="0" stop-color="var(--cyan)"/>
        <stop offset="1" stop-color="var(--mint)"/>
      </linearGradient>
      <linearGradient id="tri-bottom" x1="0" y1="0" x2="1" y2="1">
        <stop offset="0" stop-color="#3fb8cc"/>
        <stop offset="1" stop-color="#2a9a9a"/>
      </linearGradient>
    </defs>

    <circle cx="431" cy="426" r="262" fill="none" stroke="url(#ring)" stroke-width="20"/>
    <circle cx="431" cy="426" r="246" fill="url(#photo-tone)" role="img" aria-label="Photo of the two DJs posing at the decks in white T-shirts"/>

    <polygon points="146,306 626,145 536,631" fill="none" stroke="url(#tri-top)" stroke-width="14" stroke-linejoin="miter"/>
    <polygon points="310,880 768,723 682,1190" fill="none" stroke="url(#tri-bottom)" stroke-width="12" opacity="0.9"/>

    <g fill="none" stroke="#fff" stroke-width="1.5">
      <circle cx="256" cy="194" r="6"/>
      <circle cx="645" cy="220" r="6"/>
      <circle cx="401" cy="1039" r="6"/>
      <circle cx="608" cy="1110" r="6"/>
      <path d="M292 1016 l8 8 M300 1016 l-8 8"/>
      <path d="M686 1102 l7 7 M693 1102 l-7 7"/>
      <path d="M564 166 v12 M558 172 h12"/>
    </g>
    <g fill="#fff">
      <polygon points="756,223 768,223 762,231"/>
      <polygon points="756,235 768,235 762,243"/>
      <polygon points="756,247 768,247 762,255"/>
      <polygon points="756,259 768,259 762,267"/>
    </g>
    <g fill="var(--cyan)" opacity="0.9">
      <path d="M715 225 l4 16 16 4 -16 4 -4 16 -4 -16 -16 -4 16 -4z"/>
      <path d="M127 438 l3 13 13 3 -13 3 -3 13 -3 -13 -13 -3 13 -3z"/>
    </g>
  </svg>

  <h1 class="event-title event-title--top">THE CRIMSON</h1>
  <div class="event-title event-title--bottom">IBIZA ESCAPE</div>

  <section class="included">
    <h3 class="included-heading">What’s included?</h3>
    <ul class="included-list">
      <li>4 Nights Of Entertainment</li>
      <li>6 Parties In Total</li>
      <li>1 Boat Party</li>
      <li>1 Pool Party</li>
      <li>2 Superclub Parties</li>
      <li>1 Indoor Water Party</li>
      <li>Bottomless Drinks (Boat Party Only)</li>
      <li>An unbelievable experience</li>
      <li>1 unbeatable price.</li>
    </ul>
  </section>

  <p class="dates dates--start">FRIDAY 14TH JULY</p>
  <p class="dates dates--end">MONDAY 17TH JULY</p>

  <p class="offer offer-price">All this for 140€</p>
  <p class="offer offer-saving">(you save 50€ when you book with us)</p>
  <p class="offer offer-tickets">Tickets avaialble from</p>
  <p class="offer offer-sellers"><span class="arrows">▸▸▸▸</span>Ticketlane &amp; Gribolo</p>
</main>
</body>
</html>
```